Advertising image of hair fibres

Hi I’m needing someone to make me a graphic photo of this product so I can upload to Facebook and Instagram and website

By itself the product looks so boring

My wesbsite is www.velmorastrands.com

This product is hair fibres designed to make your hair look thicker.
I need to upload these images to my shop but I’m feeling the products by itself is so basic

I’m hoping to get a poster image of my product so I can advertise it online so clients are enticed to buy the product

The product has 6 colours

Target Market(s)

Men and woman

Industry/Entity Type

Beauty

Requirements
Must have
• The products and hair colours in the image
Nice to have
• Please check my website at www.velmorastrands.com to view the theme

```html
<!DOCTYPE html>
<html lang="en">
<head>
<meta charset="utf-8">
<title>Hair-Building Fibre – Ad Set</title>
<link rel="stylesheet" href="https://fonts.googleapis.com/css2?family=Montserrat:wght@300;400;500;600&display=swap">
<style>
  :root{
    --board:#aaaaaa;
    --navy:#121923;
    --sky:#7dc5e8;
    --white:#ffffff;
    --floor:#f3f6f9;
    --label-ink:#2b2b2b;
    --product-dark:#181c21;
    --product-light:#e6e9ec;
  }
  html,body{margin:0;padding:0;overflow:hidden;}
  body{width:1200px;height:1147px;background:var(--board);position:relative;font-family:"Montserrat",sans-serif;}
  .board-label{position:absolute;margin:0;font:300 20px "Montserrat",sans-serif;color:var(--label-ink);white-space:nowrap;letter-spacing:.2px;}
  .board-label--top{left:347px;top:48px;}
  .board-label--header{left:89px;top:619px;}
  .board-label--facebook{left:602px;top:617px;}
  .ad{position:absolute;display:block;}
  .ad--men{left:77px;top:111px;width:477px;height:477px;}
  .ad--women{left:596px;top:111px;width:477px;height:477px;}
  .ad--header{left:77px;top:659px;width:472px;height:326px;}
  .ad--facebook{left:596px;top:659px;width:529px;height:277px;}
  .bg{fill:var(--navy);}
  .headline{font-family:"Montserrat",sans-serif;font-weight:500;fill:var(--white);}
  .headline .accent{fill:var(--sky);font-weight:600;}
  .feature{font-family:"Montserrat",sans-serif;font-weight:400;fill:var(--white);}
  .tick{fill:none;stroke:var(--sky);stroke-width:2.6;stroke-linecap:round;stroke-linejoin:round;}
  .band{fill:var(--sky);}
  .floor{fill:var(--floor);}
  .frame{fill:var(--sky);}
  .tag{fill:var(--sky);}
  .tag-text{font-family:"Montserrat",sans-serif;font-weight:400;fill:var(--white);}
  .product-dark{fill:url(#dark-item);}
  .product-light{fill:url(#light-item);}
</style>
</head>
<body>

<p class="board-label board-label--top">For website product image, Instagram/Facebook</p>
<p class="board-label board-label--header">Homepage Header</p>
<p class="board-label board-label--facebook">Facebook Post</p>

<svg width="0" height="0" style="position:absolute">
  <defs>
    <linearGradient id="waves" x1="0" y1="0" x2="1" y2="1">
      <stop offset="0" stop-color="#7dc5e8" stop-opacity="0"/>
      <stop offset=".5" stop-color="#7dc5e8" stop-opacity=".1"/>
      <stop offset="1" stop-color="#7dc5e8" stop-opacity="0"/>
    </linearGradient>
    <linearGradient id="men-photo" x1="0" y1="0" x2="0" y2="1">
      <stop offset="0" stop-color="#4a3426"/>
      <stop offset=".7" stop-color="#6b5040"/>
      <stop offset="1" stop-color="#d9c3b3"/>
    </linearGradient>
    <linearGradient id="women-photo" x1="0" y1="0" x2="1" y2="1">
      <stop offset="0" stop-color="#a07a5c"/>
      <stop offset=".6" stop-color="#c49d80"/>
      <stop offset="1" stop-color="#8a6448"/>
    </linearGradient>
    <linearGradient id="dark-item" x1="0" y1="0" x2="1" y2="0">
      <stop offset="0" stop-color="#0d1014"/>
      <stop offset=".5" stop-color="#2a3037"/>
      <stop offset="1" stop-color="#0d1014"/>
    </linearGradient>
    <linearGradient id="light-item" x1="0" y1="0" x2="1" y2="0">
      <stop offset="0" stop-color="#c9ced3"/>
      <stop offset=".5" stop-color="#f7f8f9"/>
      <stop offset="1" stop-color="#c9ced3"/>
    </linearGradient>
  </defs>
</svg>

<!-- Product ad: men -->
<svg class="ad ad--men" viewBox="0 0 780 780" role="group" aria-label="Hair-building fibre ad for men">
  <rect class="bg" width="780" height="780"/>
  <rect x="380" y="0" width="400" height="110" fill="url(#waves)" role="img" aria-label="Flowing wave line pattern"/>
  <path class="band" d="M0,484 Q140,470 330,530 Q610,630 760,780 L0,780Z"/>
  <path class="floor" d="M0,512 Q140,500 320,556 Q590,650 735,780 L0,780Z"/>
  <text class="headline" font-size="37"><tspan x="54" y="112">HAIR - BUILDING</tspan><tspan x="54" y="162">FIBRE FOR <tspan class="accent">THICKER</tspan>,</tspan><tspan x="54" y="212"><tspan class="accent">FULLER</tspan> HAIR</tspan></text>
  <g class="feature" font-size="20">
    <path class="tick" d="M51,249 l6,6 l10,-13"/><text x="81" y="256">Spray Applicator</text>
    <path class="tick" d="M51,282 l6,6 l10,-13"/><text x="81" y="289">Hairline Optimizer Comb,</text>
    <path class="tick" d="M51,315 l6,6 l10,-13"/><text x="81" y="322">Hair Fiber Holding Spray (100ml)</text>
    <path class="tick" d="M51,348 l6,6 l10,-13"/><text x="81" y="355">Travel size (0,88 oz/25g)</text>
    <text x="81" y="382">Hair Building Fiber.</text>
  </g>
  <rect class="frame" x="471" y="122" width="213" height="241" rx="26"/>
  <rect x="480" y="122" width="204" height="232" fill="url(#men-photo)" role="img" aria-label="Photo: thinning crown on a man's head, before"/>
  <rect class="frame" x="533" y="300" width="211" height="239" rx="26"/>
  <rect x="542" y="300" width="202" height="230" rx="20" fill="url(#men-photo)" role="img" aria-label="Photo: same crown looking full after applying fibres"/>
  <g role="img" aria-label="Product photo: spray applicator, fibre bottle, holding spray and hairline comb">
    <rect class="product-dark" x="45" y="518" width="165" height="205" rx="60"/>
    <rect class="product-light" x="310" y="410" width="94" height="323" rx="12"/>
    <rect class="product-dark" x="209" y="450" width="80" height="283" rx="10"/>
    <rect class="product-dark" x="388" y="540" width="150" height="198" rx="60"/>
  </g>
  <rect class="tag" x="607" y="566" width="173" height="32"/>
  <text class="tag-text" x="693" y="590" font-size="20" text-anchor="middle" letter-spacing="1">FOR MEN</text>
</svg>

<!-- Product ad: women -->
<svg class="ad ad--women" viewBox="0 0 780 780" role="group" aria-label="Hair-building fibre ad for women">
  <rect class="bg" width="780" height="780"/>
  <rect x="380" y="0" width="400" height="110" fill="url(#waves)" role="img" aria-label="Flowing wave line pattern"/>
  <path class="band" d="M0,484 Q140,470 330,530 Q610,630 760,780 L0,780Z"/>
  <path class="floor" d="M0,512 Q140,500 320,556 Q590,650 735,780 L0,780Z"/>
  <text class="headline" font-size="37"><tspan x="54" y="112">HAIR - BUILDING</tspan><tspan x="54" y="162">FIBRE FOR <tspan class="accent">THICKER</tspan>,</tspan><tspan x="54" y="212"><tspan class="accent">FULLER</tspan> HAIR</tspan></text>
  <g class="feature" font-size="20">
    <path class="tick" d="M51,249 l6,6 l10,-13"/><text x="81" y="256">Spray Applicator</text>
    <path class="tick" d="M51,282 l6,6 l10,-13"/><text x="81" y="289">Hairline Optimizer Comb,</text>
    <path class="tick" d="M51,315 l6,6 l10,-13"/><text x="81" y="322">Hair Fiber Holding Spray (100ml)</text>
    <path class="tick" d="M51,348 l6,6 l10,-13"/><text x="81" y="355">Travel size (0,88 oz/25g)</text>
    <text x="81" y="382">Hair Building Fiber.</text>
  </g>
  <rect class="frame" x="471" y="122" width="213" height="241" rx="26"/>
  <rect x="480" y="122" width="204" height="232" fill="url(#women-photo)" role="img" aria-label="Photo: woman parting her hair to show a thin part line, before"/>
  <rect class="frame" x="533" y="300" width="211" height="239" rx="26"/>
  <rect x="542" y="300" width="202" height="230" rx="20" fill="url(#women-photo)" role="img" aria-label="Photo: same part line looking full after applying fibres"/>
  <g role="img" aria-label="Product photo: spray applicator, fibre bottle, holding spray and hairline comb">
    <rect class="product-dark" x="45" y="518" width="165" height="205" rx="60"/>
    <rect class="product-light" x="310" y="410" width="94" height="323" rx="12"/>
    <rect class="product-dark" x="209" y="450" width="80" height="283" rx="10"/>
    <rect class="product-dark" x="388" y="540" width="150" height="198" rx="60"/>
  </g>
  <rect class="tag" x="607" y="566" width="173" height="32"/>
  <text class="tag-text" x="693" y="590" font-size="20" text-anchor="middle" letter-spacing="1">FOR WOMEN</text>
</svg>

<!-- Homepage header -->
<svg class="ad ad--header" viewBox="0 0 772 534" role="group" aria-label="Homepage header banner">
  <rect class="bg" width="772" height="534"/>
  <rect x="360" y="0" width="412" height="95" fill="url(#waves)" role="img" aria-label="Flowing wave line pattern"/>
  <path class="band" d="M0,304 Q120,292 280,340 Q480,410 575,534 L0,534Z"/>
  <path class="floor" d="M0,322 Q120,312 270,358 Q460,425 555,534 L0,534Z"/>
  <text class="headline" font-size="25"><tspan x="56" y="78">HAIR - BUILDING FIBRE</tspan><tspan x="56" y="113" textLength="358" lengthAdjust="spacingAndGlyphs">FOR <tspan class="accent">THICKER</tspan>, <tspan class="accent">FULLER</tspan> HAIR</tspan></text>
  <g class="feature" font-size="14">
    <path class="tick" d="M59,140 l4,4 l7,-9"/><text x="80" y="148">Spray Applicator</text>
    <path class="tick" d="M59,163 l4,4 l7,-9"/><text x="80" y="171">Hairline Optimizer Comb,</text>
    <path class="tick" d="M59,186 l4,4 l7,-9"/><text x="80" y="194">Hair Fiber Holding Spray (100ml)</text>
    <path class="tick" d="M59,209 l4,4 l7,-9"/><text x="80" y="217">Travel size (0,88 oz/25g)</text>
    <text x="80" y="236">Hair Building Fiber.</text>
  </g>
  <rect class="frame" x="423" y="116" width="122" height="140" rx="14"/>
  <rect x="428" y="116" width="117" height="135" fill="url(#women-photo)" role="img" aria-label="Photo: woman's thin part line, before"/>
  <rect class="frame" x="453" y="219" width="128" height="140" rx="16"/>
  <rect x="458" y="219" width="123" height="135" rx="12" fill="url(#women-photo)" role="img" aria-label="Photo: woman's part line filled in, after"/>
  <rect class="frame" x="557" y="75" width="128" height="139" rx="14"/>
  <rect x="562" y="75" width="123" height="134" fill="url(#men-photo)" role="img" aria-label="Photo: man's thinning crown, before"/>
  <rect class="frame" x="592" y="179" width="129" height="139" rx="16"/>
  <rect x="597" y="179" width="124" height="134" rx="12" fill="url(#men-photo)" role="img" aria-label="Photo: man's crown looking full, after"/>
  <g role="img" aria-label="Product photo: spray applicator, fibre bottle, holding spray and hairline comb">
    <rect class="product-dark" x="32" y="326" width="130" height="155" rx="45"/>
    <rect class="product-light" x="224" y="249" width="70" height="237" rx="9"/>
    <rect class="product-dark" x="149" y="278" width="72" height="208" rx="8"/>
    <rect class="product-dark" x="296" y="346" width="96" height="145" rx="40"/>
  </g>
  <rect class="tag" x="469" y="373" width="106" height="21"/>
  <text class="tag-text" x="522" y="389" font-size="14" text-anchor="middle" letter-spacing=".6">FOR WOMEN</text>
  <rect class="tag" x="609" y="339" width="101" height="20"/>
  <text class="tag-text" x="659" y="354" font-size="14" text-anchor="middle" letter-spacing=".6">FOR MEN</text>
</svg>

<!-- Facebook post -->
<svg class="ad ad--facebook" viewBox="0 0 866 453" role="group" aria-label="Facebook post banner">
  <rect class="bg" width="866" height="453"/>
  <rect x="500" y="0" width="366" height="75" fill="url(#waves)" role="img" aria-label="Flowing wave line pattern"/>
  <path class="band" d="M0,250 Q130,238 300,282 Q500,345 610,453 L0,453Z"/>
  <path class="floor" d="M0,268 Q130,258 290,300 Q480,360 590,453 L0,453Z"/>
  <text class="headline" font-size="25"><tspan x="57" y="60">HAIR - BUILDING FIBRE</tspan><tspan x="57" y="95">FOR <tspan class="accent">THICKER</tspan>, <tspan class="accent">FULLER</tspan> HAIR</tspan></text>
  <g class="feature" font-size="14">
    <path class="tick" d="M55,117 l4,4 l7,-9"/><text x="72" y="123">Spray Applicator</text>
    <path class="tick" d="M197,117 l4,4 l7,-9"/><text x="214" y="123">Hairline Optimizer Comb,</text>
    <path class="tick" d="M55,136 l4,4 l7,-9"/><text x="72" y="142">Hair Fiber Holding Spray (100ml)</text>
    <path class="tick" d="M55,155 l4,4 l7,-9"/><text x="72" y="161">Travel size (0,88 oz/25g) Hair Building Fiber.</text>
  </g>
  <rect class="frame" x="526" y="96" width="122" height="140" rx="14"/>
  <rect x="531" y="96" width="117" height="135" fill="url(#women-photo)" role="img" aria-label="Photo: woman's thin part line, before"/>
  <rect class="frame" x="556" y="201" width="128" height="139" rx="16"/>
  <rect x="561" y="201" width="123" height="134" rx="12" fill="url(#women-photo)" role="img" aria-label="Photo: woman's part line filled in, after"/>
  <rect class="frame" x="662" y="55" width="127" height="141" rx="14"/>
  <rect x="667" y="55" width="122" height="136" fill="url(#men-photo)" role="img" aria-label="Photo: man's thinning crown, before"/>
  <rect class="frame" x="699" y="159" width="125" height="139" rx="16"/>
  <rect x="704" y="159" width="120" height="134" rx="12" fill="url(#men-photo)" role="img" aria-label="Photo: man's crown looking full, after"/>
  <g role="img" aria-label="Product photo: spray applicator, fibre bottle, holding spray and hairline comb">
    <rect class="product-dark" x="46" y="266" width="118" height="155" rx="42"/>
    <rect class="product-light" x="239" y="186" width="70" height="240" rx="9"/>
    <rect class="product-dark" x="164" y="214" width="72" height="207" rx="8"/>
    <rect class="product-dark" x="300" y="281" width="112" height="145" rx="42"/>
  </g>
  <rect class="tag" x="571" y="353" width="107" height="21"/>
  <text class="tag-text" x="624" y="369" font-size="14" text-anchor="middle" letter-spacing=".6">FOR WOMEN</text>
  <rect class="tag" x="712" y="318" width="101" height="21"/>
  <text class="tag-text" x="762" y="334" font-size="14" text-anchor="middle" letter-spacing=".6">FOR MEN</text>
</svg>

</body>
</html>
```